VOLMA Presentation (Crescent Studies & Learning Academy)

We need a befitting corporate presentation for an international institute affiliated to a multilateral development bank based in Jeddah, Saudi Arabia. The institute primarily provides research, capacity development, knowledge-based solutions, and publications in Islamic Economics, Banking & Finance. Our services target mainly banking and financial institutions, regulatory authorities, other multi-laterals, academic institutions, and other institutions and personnel involved with development activities. The corporate presentation should reflect our vision and rich historical past. We have attached here a draft of the presentation. We need it beautifully re-designed with lots of graphics and animations. If any additional information is required, please contact us.
Updates

Please note that final project must be provided to us in PowerPoint Presentation format. Thank you.

Colors

Designer to choose colors to be used in the design.

Requirements
Must have
• Final project must be submitted to us in PowerPoint Presentation (.ppt) format.
Nice to have
• Suitable clip art images in slides containing lists or itemized content.

```html
<!DOCTYPE html>
<html lang="en">
<head>
<meta charset="utf-8">
<title>VOLMA Presentation</title>
<link href="https://fonts.googleapis.com/css2?family=Roboto:wght@400;500;700;900&display=swap" rel="stylesheet">
<style>
:root{
  --canvas:#e4e2e2;
  --green-dark:#1b5a2c;
  --green:#2e9a3c;
  --green-mid:#23763a;
  --olive:#9c9b2b;
  --navy:#243370;
  --gray:#8a8a8a;
  --ink:#1d2b22;
  --white:#fff;
}
*{margin:0;padding:0;box-sizing:border-box}
html,body{width:793px;height:1200px;overflow:hidden;background:var(--canvas);font-family:"Roboto",Arial,sans-serif;color:var(--ink)}
.deck{position:relative;width:793px;height:1200px}
.slide{position:absolute;width:246px;height:138px;background:var(--white);overflow:hidden}
.c1{left:16px}.c2{left:272px}.c3{left:528px}
.r1{top:17px}.r2{top:161px}.r3{top:308px}.r4{top:455px}.r5{top:601px}.r6{top:748px}.r7{top:895px}.r8{top:1041px}
.foot{position:absolute;left:0;right:0;bottom:0;height:5px;background:var(--green-dark)}
.foot::after{content:"";position:absolute;right:6px;top:-3px;width:8px;height:8px;border-radius:50%;background:var(--green)}
.foot-mark{position:absolute;left:6px;bottom:2px;font-size:4px;font-weight:900;color:var(--green-dark)}
.abs{position:absolute}
.title{position:absolute;left:0;right:0;text-align:center;font-weight:700;color:var(--green-dark);font-size:11.5px;letter-spacing:.2px}
.photo{position:absolute}
.band{position:absolute;background:var(--green);color:var(--white);font-weight:700;line-height:1.1}
.tiny{font-size:4px;line-height:1.25}
.small{font-size:5px;line-height:1.25}
.brand{font-weight:900;color:var(--green-dark)}
.ctr{text-align:center}
</style>
</head>
<body>
<div class="deck">

<!-- 1 cover -->
<section class="slide c1 r1">
  <div class="photo" role="img" aria-label="Financial data screen background" style="left:0;top:0;width:246px;height:105px;background:linear-gradient(120deg,#3a2b2f,#1b3550 55%,#123a55)"></div>
  <div class="abs ctr" style="left:0;right:0;top:50px;color:#fff;font-weight:700;font-size:8.6px">CRESCENT STUDIES &amp; LEARNING ACADEMY<br><span style="font-size:5.5px;font-weight:400">( VOLMA )</span></div>
  <div class="abs" style="left:96px;top:92px;color:#fff;font-weight:700;font-size:8px">www.volma.org</div>
  <div class="abs brand" style="left:8px;top:116px;font-size:8px">VOLMA</div>
  <div class="abs ctr" style="left:70px;top:113px;width:110px;font-size:5.5px;font-weight:500;color:var(--green-dark)">Member of the<br>Meridian Development Bank Group</div>
  <div class="abs" style="left:207px;top:108px;width:26px;height:26px;border-radius:50%;background:var(--green)"></div>
</section>

<!-- 2 cover alt -->
<section class="slide c2 r1">
  <div class="photo" role="img" aria-label="Curved city skyline panel" style="left:0;top:0;width:160px;height:138px;background:linear-gradient(135deg,#2b1d24,#17284a 60%,#0f1e3a);clip-path:ellipse(100% 120% at 0% 50%)"></div>
  <div class="abs brand" style="left:146px;top:14px;font-size:8px">VOLMA</div>
  <div class="abs ctr" style="left:84px;top:50px;width:156px;font-weight:700;color:var(--green-dark);font-size:7.4px">CRESCENT STUDIES &amp; LEARNING<br>ACADEMY<br><span style="font-size:4.5px;font-weight:400">( VOLMA )</span></div>
  <div class="abs" style="left:3px;top:124px;color:#fff;font-weight:700;font-size:7px">www.volma.org</div>
  <div class="abs" style="left:186px;top:112px;width:10px;height:10px;border-radius:50%;background:var(--green)"></div>
  <div class="abs ctr tiny" style="left:160px;top:124px;width:80px">Member of the<br>Meridian Development Bank Group</div>
</section>

<!-- 3 group -->
<section class="slide c3 r1">
  <div class="title" style="top:8px">MDB GROUP</div>
  <svg class="abs" style="left:0;top:0" width="246" height="138" viewBox="0 0 246 138">
    <g font-size="5" fill="#fff" text-anchor="middle" font-weight="700">
      <path d="M62,126 A62,62 0 0 1 72,90 L100,105 A30,30 0 0 0 94,126Z" fill="var(--navy)"/><text x="74" y="113">1981</text>
      <path d="M76,84 A62,62 0 0 1 106,62 L114,90 A30,30 0 0 0 102,100Z" fill="var(--green-dark)"/><text x="94" y="80">1994</text>
      <path d="M113,60 A62,62 0 0 1 138,60 L131,89 A30,30 0 0 0 119,89Z" fill="#1e3d5c"/><text x="125" y="70">1999</text>
      <path d="M145,62 A62,62 0 0 1 174,84 L148,100 A30,30 0 0 0 137,90Z" fill="var(--green)"/><text x="155" y="80">2005</text>
      <path d="M178,90 A62,62 0 0 1 188,126 L156,126 A30,30 0 0 0 150,105Z" fill="var(--olive)"/><text x="175" y="113">2008</text>
    </g>
    <text x="125" y="117" text-anchor="middle" font-size="10" font-weight="700" fill="var(--navy)">MDB</text>
    <text x="125" y="124" text-anchor="middle" font-size="3.5" fill="var(--navy)">Meridian Development Bank</text>
    <g font-size="8" font-weight="900" fill="var(--green-dark)"><text x="36" y="58">CIEX</text><text x="128" y="40" fill="var(--green-dark)">CPS</text><text x="198" y="52">SFD</text><text x="200" y="100">CTFC</text><text x="34" y="102">VOLMA</text></g>
    <g font-size="3.2" fill="var(--green-dark)" text-anchor="middle">
      <text x="48" y="66">Corporation for Insurance of</text><text x="48" y="70">Investment and Export Credit</text>
      <text x="108" y="34">Corporation for Private Sector</text>
      <text x="210" y="60">Solidarity Fund for Development</text>
      <text x="212" y="108">Trade Finance Corporation</text>
      <text x="50" y="110">Studies &amp; Learning Academy</text>
    </g>
  </svg>
  <div class="foot"></div>
</section>

<!-- 4 milestones -->
<section class="slide c1 r2">
  <div class="title" style="top:20px">VOLMA MILESTONES</div>
  <svg class="abs" style="left:0;top:0" width="246" height="138" viewBox="0 0 246 138">
    <rect x="0" y="78" width="246" height="6" fill="var(--green-dark)"/>
    <g font-size="4" fill="#fff" text-anchor="middle" font-weight="700">
      <text x="10" y="82.5">1981</text><text x="30" y="82.5">1983</text><text x="50" y="82.5">1988</text><text x="70" y="82.5">2003</text><text x="90" y="82.5">2004</text><text x="110" y="82.5">2005</text><text x="130" y="82.5">2008</text><text x="150" y="82.5">2008</text><text x="170" y="82.5">2009</text><text x="190" y="82.5">2009</text><text x="210" y="82.5">2010</text><text x="230" y="82.5">2011</text>
    </g>
    <g font-size="3" fill="var(--ink)" text-anchor="middle">
      <text x="30" y="66">Operational</text>
      <text x="70" y="60">Became MDB</text><text x="70" y="64">Group Entity</text>
      <text x="110" y="56">Launched</text><text x="110" y="60">Distance</text><text x="110" y="64">Learning</text>
      <text x="150" y="56">Established</text><text x="150" y="60">Advisory</text><text x="150" y="64">Division</text>
      <text x="190" y="60">Launched VOLMA</text><text x="190" y="64">Scholarship</text>
      <text x="230" y="52">Launched E-</text><text x="230" y="56">Learning –</text><text x="230" y="60">Masters in</text><text x="230" y="64">Finance</text>
      <text x="10" y="98">Established</text>
      <text x="50" y="98">Launched MDB</text><text x="50" y="102">Prize</text>
      <text x="90" y="98">Launched CBIS</text>
      <text x="130" y="98">Launched MDB</text><text x="130" y="102">Solidarity Prize –</text><text x="130" y="106">Promotion of</text><text x="130" y="110">Trade among</text><text x="130" y="114">member states</text>
      <text x="170" y="98">Launched VOLMA</text><text x="170" y="102">Research Grants</text>
      <text x="210" y="98">Launched</text><text x="210" y="102">Global</text><text x="210" y="106">Leadership</text><text x="210" y="110">Programme</text>
    </g>
    <g fill="none" stroke="var(--green)" stroke-width="1"><path d="M28,72 l2,-2 l2,2M68,72 l2,-2 l2,2M108,72 l2,-2 l2,2M148,72 l2,-2 l2,2M188,72 l2,-2 l2,2M228,72 l2,-2 l2,2"/></g>
    <g fill="none" stroke="var(--green-dark)" stroke-width="1"><path d="M8,88 l2,2 l2,-2M48,88 l2,2 l2,-2M88,88 l2,2 l2,-2M128,88 l2,2 l2,-2M168,88 l2,2 l2,-2M208,88 l2,2 l2,-2"/></g>
  </svg>
  <div class="foot"></div>
</section>

<!-- 5 about section -->
<section class="slide c2 r2">
  <div class="photo" role="img" aria-label="Stacked coins over financial charts" style="left:80px;top:0;width:166px;height:138px;background:linear-gradient(90deg,#f3f1ec,#b08a4d 55%,#6d5127)"></div>
  <div class="abs brand" style="left:22px;top:46px;font-size:14px">VOLMA</div>
  <div class="abs ctr tiny" style="left:8px;top:68px;width:70px;color:var(--green-dark)">CRESCENT STUDIES &amp; LEARNING ACADEMY</div>
  <div class="band" style="left:0;top:99px;width:246px;height:24px;background:var(--green-dark);padding:5px 14px;font-size:14px">ABOUT VOLMA</div>
</section>

<!-- 6 about -->
<section class="slide c3 r2">
  <div class="abs" style="left:10px;top:48px;font-weight:700;font-size:14px;color:var(--green-dark);line-height:1.15;text-align:center">ABOUT<br>VOLMA</div>
  <svg class="abs" style="left:0;top:0" width="246" height="138" viewBox="0 0 246 138">
    <polygon points="66,64 108,12 110,34" fill="var(--green-dark)"/>
    <polygon points="66,66 108,38 108,62" fill="var(--gray)"/>
    <polygon points="66,70 108,68 108,92" fill="var(--green-dark)"/>
    <polygon points="66,72 108,96 110,122" fill="var(--gray)"/>
  </svg>
  <div class="abs ctr tiny" style="left:106px;top:12px;width:134px;height:22px;background:var(--green);color:#fff;padding:2px">The Academy is responsible for knowledge creation and dissemination in economics and finance to support development of member countries.</div>
  <div class="abs ctr tiny" style="left:106px;top:38px;width:134px;height:24px;background:var(--gray);color:#fff;padding:4px">We lead in providing innovative, knowledge-based solutions for development challenges facing member countries.</div>
  <div class="abs ctr tiny" style="left:106px;top:68px;width:134px;height:24px;background:var(--green);color:#fff;padding:5px">We lead in providing learning and capacity building for member countries to achieve the SDGs.</div>
  <div class="abs ctr tiny" style="left:106px;top:96px;width:134px;height:26px;background:var(--gray);color:#fff;padding:3px">As global leaders we work with partners to deliver research, enhance human capital and provide information services worldwide.</div>
  <div class="foot"></div>
</section>

<!-- 7 numbers -->
<section class="slide c1 r3">
  <div class="title" style="top:12px">VOLMA IN NUMBERS (1981-2019)</div>
  <svg class="abs" style="left:0;top:0" width="246" height="138" viewBox="0 0 246 138">
    <g stroke="#e6e6e6" stroke-width="2.5">
      <circle cx="44" cy="46" r="11" fill="var(--green-dark)"/><circle cx="93" cy="46" r="11" fill="var(--green)"/><circle cx="145" cy="46" r="11" fill="var(--green-dark)"/><circle cx="198" cy="46" r="11" fill="var(--green)"/>
      <circle cx="44" cy="95" r="11" fill="var(--green)"/><circle cx="93" cy="95" r="11" fill="var(--green-dark)"/><circle cx="145" cy="95" r="11" fill="var(--green)"/><circle cx="198" cy="95" r="11" fill="var(--green-dark)"/>
    </g>
    <g stroke="#fff" stroke-width="1.2" fill="none">
      <circle cx="43" cy="45" r="3.5"/><path d="M46,48 l3,3"/>
      <circle cx="93" cy="46" r="5"/><path d="M88,46h10M93,41v10"/>
      <rect x="139" y="41" width="12" height="9"/><path d="M141,48l3,-3l2,2l3,-3"/>
      <rect x="192" y="41" width="12" height="8"/><path d="M198,49v3M195,52h6"/>
      <path d="M38,100v-10M38,100h12M40,98l3,-4l2,2l4,-5"/>
      <path d="M89,88h8v4a4,4 0 0 1 -8,0zM93,96v3M90,100h6"/>
      <circle cx="145" cy="93" r="4"/><path d="M143,99h4"/>
      <path d="M192,90h5v10h-5zM199,90h5v10h-5z"/>
    </g>
    <g font-size="4.6" text-anchor="middle" fill="var(--ink)" font-weight="500">
      <text x="44" y="65">377</text><text x="93" y="65">405</text><text x="145" y="65">729</text><text x="198" y="65">8</text>
      <text x="44" y="114">19</text><text x="93" y="114">63</text><text x="145" y="114">23</text><text x="198" y="114">513</text>
    </g>
    <g font-size="3.2" text-anchor="middle" fill="var(--ink)">
      <text x="44" y="70">RESEARCH PROJECTS</text><text x="93" y="70">CONFERENCES</text><text x="145" y="70">TRAINING PROGRAMS</text><text x="198" y="70">ONLINE LEARNING</text><text x="198" y="74">PROGRAMS</text>
      <text x="44" y="119">ADVISORY PROJECTS</text><text x="93" y="119">ENCOURAGEMENT</text><text x="93" y="123">PROGRAMS</text><text x="145" y="119">KNOWLEDGE</text><text x="145" y="123">DISSEMINATION</text><text x="198" y="119">PUBLICATIONS</text>
    </g>
  </svg>
  <div class="foot"></div>
</section>

<!-- 8 what we do -->
<section class="slide c2 r3">
  <div class="abs ctr" style="left:10px;top:42px;font-weight:700;font-size:21px;color:var(--green-dark);line-height:1.25">WHAT<br>WE DO</div>
  <svg class="abs" style="left:0;top:0" width="246" height="138" viewBox="0 0 246 138">
    <polygon points="145,3 200,3 225,38 145,38" fill="var(--green-dark)"/>
    <polygon points="108,78 123,8 142,3 142,90" fill="#fff" stroke="#e2e2e2"/>
    <polygon points="108,80 196,80 196,128 142,128" fill="var(--green-dark)"/>
    <polygon points="198,42 226,42 226,93 198,126" fill="#fff" stroke="#e2e2e2"/>
  </svg>
  <div class="abs" style="left:150px;top:18px;color:#fff;font-size:5.5px;font-weight:500">Capacity Development</div>
  <div class="abs ctr" style="left:104px;top:53px;width:44px;font-size:5.5px">Knowledge<br>Solutions</div>
  <div class="abs ctr" style="left:146px;top:58px;width:52px;font-size:8px;font-weight:500;color:var(--green-dark)">VOLMA<br>ACTIVITIES</div>
  <div class="abs ctr" style="left:196px;top:67px;width:32px;font-size:5.5px;color:var(--green-dark)">Innovative<br>Research</div>
  <div class="abs" style="left:130px;top:104px;width:64px;text-align:right;color:#fff;font-size:5.5px">Publications &amp;<br>Information Services</div>
  <div class="foot"></div>
</section>

<!-- 9 innovative research section -->
<section class="slide c3 r3">
  <div class="photo" role="img" aria-label="Person working on a laptop" style="left:0;top:0;width:246px;height:138px;background:linear-gradient(135deg,#1f2a33,#4d5a63 50%,#1b242c)"></div>
  <div class="band" style="left:64px;top:46px;width:182px;height:44px;padding:5px 7px;font-size:14px;background:var(--green)">INNOVATIVE<br>RESEARCH</div>
</section>

<!-- 10 innovative research -->
<section class="slide c1 r4">
  <div class="title" style="top:12px">INNOVATIVE RESEARCH</div>
  <div class="abs ctr small" style="left:14px;top:37px;width:216px;height:24px;background:var(--green-dark);color:#fff;padding:4px 10px">We are a pioneer in conducting, promoting and encouraging research innovation and knowledge creation in Economics, Banking and Finance.</div>
  <div class="abs ctr small" style="left:14px;top:64px;width:216px;height:25px;border:1.2px solid var(--green-dark);padding:5px 10px 0 34px">Our research seeks to identify challenges of economic development facing member countries.</div>
  <div class="abs ctr small" style="left:14px;top:93px;width:216px;height:25px;border:1.2px solid var(--green-dark);padding:5px 10px 0 34px">Our research formulates solutions and strategies for addressing the challenges in accordance with its guiding principles.</div>
  <svg class="abs" style="left:18px;top:66px" width="20" height="52" viewBox="0 0 20 52"><circle cx="10" cy="10" r="9" fill="var(--green-dark)"/><circle cx="10" cy="40" r="9" fill="var(--green-dark)"/><path d="M6,10l3,3l5,-6M6,40l3,3l5,-6" stroke="#fff" stroke-width="1.4" fill="none"/></svg>
  <div class="foot"></div>
</section>

<!-- 11 research products -->
<section class="slide c2 r4">
  <div class="title" style="top:16px">RESEARCH PRODUCTS &amp; SERVICES</div>
  <svg class="abs" style="left:0;top:0" width="246" height="138" viewBox="0 0 246 138">
    <g fill="none" stroke-width="6"><circle cx="46" cy="76" r="26" stroke="var(--green-dark)"/><circle cx="99" cy="76" r="26" stroke="var(--green)"/><circle cx="152" cy="76" r="26" stroke="var(--green-dark)"/><circle cx="205" cy="76" r="26" stroke="var(--green)"/></g>
    <g font-size="4.6" text-anchor="middle" fill="var(--ink)" font-weight="500">
      <text x="46" y="72">In-house</text><text x="46" y="77">and Joint</text><text x="46" y="82">Research</text>
      <text x="99" y="63">Research</text><text x="99" y="68">products</text><text x="99" y="74">(journals,</text><text x="99" y="80">books, reports,</text><text x="99" y="86">lectures, etc.)</text>
      <text x="152" y="63">Research</text><text x="152" y="68">Events</text><text x="152" y="73">(conferences,</text><text x="152" y="79">workshops,</text><text x="152" y="85">symposiums,</text><text x="152" y="91">etc.)</text>
      <text x="205" y="78">MDB Prize</text>
    </g>
  </svg>
  <div class="foot"></div>
</section>

<!-- 12 research areas -->
<section class="slide c3 r4">
  <svg class="abs" style="left:0;top:0" width="246" height="138" viewBox="0 0 246 138">
    <circle cx="119" cy="74" r="34" fill="none" stroke="var(--green-dark)" stroke-width="4"/>
    <g stroke-width="4" fill="none">
      <path d="M119,38v-14" stroke="var(--green-dark)"/><path d="M143,50l10,-8" stroke="var(--green)"/><path d="M153,74h14" stroke="var(--green-dark)"/><path d="M143,98l8,8" stroke="var(--olive)"/>
      <path d="M119,108v14" stroke="var(--green)"/><path d="M95,98l-10,8" stroke="var(--green-dark)"/><path d="M85,74h-14" stroke="var(--olive)"/><path d="M95,50l-8,-8" stroke="var(--green)"/>
    </g>
    <g><polygon points="114,24 124,24 119,16" fill="var(--green-dark)"/><polygon points="150,38 158,40 156,47" fill="var(--green)"/><polygon points="167,69 167,79 174,74" fill="var(--green-dark)"/><polygon points="155,104 148,108 154,112" fill="var(--olive)"/><polygon points="114,122 124,122 119,130" fill="var(--green)"/><polygon points="88,110 82,102 80,110" fill="var(--green-dark)"/><polygon points="71,69 71,79 64,74" fill="var(--olive)"/><polygon points="84,38 92,40 86,46" fill="var(--green)"/></g>
    <text x="119" y="72" text-anchor="middle" font-size="8" font-weight="500" fill="var(--green-dark)">RESEARCH</text>
    <text x="119" y="81" text-anchor="middle" font-size="8" font-weight="500" fill="var(--green-dark)">AREAS</text>
    <g font-size="5" font-weight="500" fill="var(--ink)">
      <text x="96" y="10">Smart Economy</text>
      <text x="26" y="25">Innovation and</text><text x="24" y="31">Entrepreneurship</text>
      <text x="164" y="30">Social Finance</text>
      <text x="12" y="66">Management in</text><text x="3" y="72">Capital Market</text>
      <text x="180" y="77">Banking</text>
      <text x="26" y="110">Shariah Structuring</text>
      <text x="159" y="111">Awqaf</text>
      <text x="102" y="128">Capital Market</text>
    </g>
  </svg>
  <div class="foot"></div>
</section>

<!-- 13 capacity section -->
<section class="slide c1 r5">
  <div class="photo" role="img" aria-label="Hand holding a network of connected people" style="left:0;top:0;width:246px;height:138px;background:linear-gradient(135deg,#1d3441,#3d5d69 55%,#1a2d36)"></div>
  <div class="band" style="left:64px;top:46px;width:182px;height:44px;padding:5px 8px;font-size:14px">CAPACITY<br>DEVELOPMENT</div>
</section>

<!-- 14 capacity dev -->
<section class="slide c2 r5">
  <div class="title" style="top:10px">CAPACITY DEVELOPMENT</div>
  <div class="abs" style="left:0;top:27px;width:132px;height:94px;background:var(--green-mid)"></div>
  <div class="photo" role="img" aria-label="Business handshake" style="left:132px;top:27px;width:114px;height:94px;background:linear-gradient(135deg,#d8e2ea,#8ea2b3 60%,#4a5b6a)"></div>
  <svg class="abs" style="left:8px;top:44px" width="12" height="70" viewBox="0 0 12 70"><circle cx="6" cy="6" r="5" fill="none" stroke="#fff"/><circle cx="6" cy="50" r="5" fill="none" stroke="#fff"/><path d="M3.5,6l2,2l3,-4M3.5,50l2,2l3,-4" stroke="#fff" fill="none"/></svg>
  <div class="abs small" style="left:26px;top:40px;width:100px;color:#fff;text-align:justify">VOLMA is the largest contributor to human capital development in Economics, Banking and Finance.</div>
  <div class="abs small" style="left:26px;top:77px;width:100px;color:#fff;text-align:justify">We develop human resources and technical capacity in Economics, Banking and Finance, by providing training courses by both online and face to face.</div>
  <div class="foot"></div>
</section>

<!-- 15 capacity programs -->
<section class="slide c3 r5">
  <div class="title" style="top:10px;font-size:13px">CAPACITY DEVELOPMENT</div>
  <div class="abs ctr tiny" style="left:40px;top:37px;width:60px">Programs for MDB<br>Member Countries</div>
  <div class="abs tiny" style="left:118px;top:41px">Training Packages</div>
  <div class="abs tiny" style="left:180px;top:41px">Online Learning Programs</div>
  <svg class="abs" style="left:0;top:0" width="246" height="138" viewBox="0 0 246 138" role="img" aria-label="Photos of classrooms, leaders, training, certificates and online courses">
    <polygon points="10,99 38,52 58,99" fill="#6b6f74"/>
    <polygon points="46,52 100,52 72,100" fill="#7a5a3e"/>
    <polygon points="76,99 104,52 132,99" fill="#b06b3a"/>
    <polygon points="112,52 166,52 138,100" fill="#5f7b93"/>
    <polygon points="144,99 172,52 200,99" fill="#8fb3c9"/>
    <polygon points="178,52 236,52 208,100" fill="#c9c9cf"/>
  </svg>
  <div class="abs ctr tiny" style="left:10px;top:104px;width:60px">Programs for Private<br>Sector</div>
  <div class="abs ctr tiny" style="left:76px;top:104px;width:60px">Knowledge Leaders<br>Programs</div>
  <div class="abs tiny" style="left:152px;top:104px">Certification Program</div>
  <div class="foot"></div>
</section>

<!-- 16 topics -->
<section class="slide c1 r6">
  <div class="abs" style="left:13px;top:9px;font-weight:700;font-size:11.5px;color:var(--green-dark)">TOPICS OF THE TRAINING COURSES</div>
  <svg class="abs" style="left:15px;top:32px" width="10" height="90" viewBox="0 0 10 90">
    <g fill="var(--green)"><circle cx="5" cy="4" r="4"/><circle cx="5" cy="17" r="4"/><circle cx="5" cy="30" r="4"/><circle cx="5" cy="43" r="4"/><circle cx="5" cy="56" r="4"/><circle cx="5" cy="69" r="4"/><circle cx="5" cy="82" r="4"/></g>
    <path d="M3,4l1.5,1.5l2.5,-3M3,17l1.5,1.5l2.5,-3M3,30l1.5,1.5l2.5,-3M3,43l1.5,1.5l2.5,-3M3,56l1.5,1.5l2.5,-3M3,69l1.5,1.5l2.5,-3M3,82l1.5,1.5l2.5,-3" stroke="#fff" stroke-width=".9" fill="none"/>
  </svg>
  <div class="abs" style="left:29px;top:33px;font-size:5.6px;line-height:13.1px;color:var(--green-dark)">
    Principles of Economics, Banking &amp; Finance<br>
    Regulation and Supervision of Ethical Banks<br>
    Risk Management in Financial Institutions<br>
    Shari'ah Supervision and Auditing of Financial Institutions<br>
    Sukuk: Shari'ah and Operational Aspects<br>
    Shari'ah Standards for Financial Institutions<br>
    Corporate Governance for Financial Institutions
  </div>
  <div class="foot"></div>
</section>

<!-- 17 online learning -->
<section class="slide c2 r6">
  <div class="title" style="top:10px">ONLINE LEARNING PROGRAMS</div>
  <svg class="abs" style="left:0;top:0" width="246" height="138" viewBox="0 0 246 138">
    <circle cx="36" cy="50" r="20" fill="#fff" stroke="var(--green)" stroke-width="2"/>
    <text x="36" y="49" text-anchor="middle" font-size="5.2" font-weight="700" fill="var(--green)">VOLMA on</text>
    <text x="36" y="55" text-anchor="middle" font-size="5.2" font-weight="700" fill="var(--green)">OpenCourse</text>
    <path d="M57,50h60M97,104h20" stroke="var(--green)" stroke-dasharray="2 1.5" stroke-width=".8"/>
    <rect x="13" y="78" width="82" height="38" rx="5" fill="#fff" stroke="#e5e5e5"/>
    <g fill="var(--green-dark)"><rect x="24" y="92" width="2" height="10"/><rect x="28" y="95" width="2" height="7"/><rect x="32" y="90" width="2" height="12"/><rect x="36" y="93" width="2" height="9"/></g>
    <path d="M22,88v15h19" stroke="var(--green-dark)" fill="none" stroke-width=".8"/>
    <text x="71" y="90" text-anchor="middle" font-size="9" font-weight="700" fill="var(--green)">45.000</text>
    <text x="71" y="95" text-anchor="middle" font-size="4" fill="var(--ink)">Beneficiaries</text>
    <text x="71" y="106" text-anchor="middle" font-size="8" font-weight="700" fill="var(--green)">8</text>
    <text x="71" y="111" text-anchor="middle" font-size="4" fill="var(--ink)">Courses</text>
  </svg>
  <div class="abs" role="img" aria-label="Course thumbnail cards" style="left:120px;top:26px;width:116px;height:102px">
    <svg width="116" height="102" viewBox="0 0 116 102"><g fill="#7f9aa6"><rect x="0" y="0" width="37" height="22"/><rect x="39" y="0" width="37" height="22"/><rect x="78" y="0" width="37" height="22"/><rect x="0" y="36" width="37" height="22"/><rect x="39" y="36" width="37" height="22"/><rect x="78" y="36" width="37" height="22"/><rect x="16" y="72" width="37" height="22"/><rect x="55" y="72" width="37" height="22"/></g><g fill="var(--green)"><rect x="0" y="18" width="37" height="2"/><rect x="39" y="18" width="37" height="2"/><rect x="78" y="18" width="37" height="2"/><rect x="0" y="54" width="37" height="2"/><rect x="39" y="54" width="37" height="2"/><rect x="78" y="54" width="37" height="2"/><rect x="16" y="90" width="37" height="2"/><rect x="55" y="90" width="37" height="2"/></g>
    <g font-size="2.6" fill="#666"><text x="0" y="26">Principles of Insurance</text><text x="39" y="26">Finance and Banking</text><text x="78" y="26">Capital Markets</text><text x="0" y="62">Banking Modes</text><text x="39" y="62">Insurance Investments</text><text x="78" y="62">Money Markets</text><text x="16" y="98">Capital Markets Structure</text><text x="55" y="98">Banking Principles</text></g></svg>
  </div>
  <div class="foot"></div>
</section>

<!-- 18 knowledge section -->
<section class="slide c3 r6">
  <div class="photo" role="img" aria-label="Dark gear and technology background" style="left:0;top:0;width:246px;height:138px;background:linear-gradient(135deg,#1c2126,#38414a 55%,#1a1f24)"></div>
  <div class="band" style="left:64px;top:46px;width:182px;height:44px;padding:5px 8px;font-size:14px">KNOWLEDGE<br>SOLUTIONS</div>
</section>

<!-- 19 knowledge text -->
<section class="slide c1 r7">
  <div class="photo" role="img" aria-label="Hand holding a glowing digital globe" style="left:0;top:0;width:114px;height:138px;background:radial-gradient(circle at 45% 55%,#3b6a8a,#16283a 70%)"></div>
  <div class="abs" style="left:20px;top:54px;color:#fff;font-weight:700;font-size:11px;line-height:1.3">KNOWLEDGE<br>SOLUTIONS</div>
  <div class="abs" style="left:128px;top:12px;width:106px;font-size:5.6px;line-height:11.1px;text-align:justify;color:var(--ink)">The Knowledge Solutions initiative aims to transform critical components of the economy of MDB's Member Countries using Fintech innovations and technologies (AI, Blockchain, IoT, etc.) to bring about value-based, inclusive and sustainable growth in line with principles of ethical economics and finance.</div>
  <div class="foot"></div>
</section>

<!-- 20 publications section -->
<section class="slide c2 r7">
  <div class="photo" role="img" aria-label="Library bookshelves" style="left:0;top:0;width:246px;height:138px;background:linear-gradient(180deg,#2a2d33,#46413c 50%,#25282d)"></div>
  <div class="band" style="left:64px;top:46px;width:182px;height:44px;padding:7px 4px;font-size:11.5px">PUBLICATIONS<br>&amp; INFORMATION SERVICES</div>
</section>

<!-- 21 knowledge activities -->
<section class="slide c3 r7">
  <div class="title" style="top:12px;font-size:13px">KNOWLEDGE SOLUTIONS</div>
  <div class="abs ctr" style="left:12px;top:37px;width:220px;height:26px;background:var(--green-dark);color:#fff;font-size:6.2px;font-weight:500;padding-top:9px">The main activities under Knowledge Solutions initiative are:</div>
  <div class="abs" style="left:11px;top:88px;font-weight:700;font-size:11px;color:var(--green-dark)">01</div>
  <div class="abs tiny" style="left:28px;top:80px;width:82px;text-align:justify;font-size:4.8px">Designing and structuring of new, innovative, knowledge-based solutions for development challenges of MDB's Member Countries</div>
  <div class="abs" style="left:127px;top:88px;font-weight:700;font-size:11px;color:var(--green-dark)">02</div>
  <div class="abs tiny" style="left:144px;top:80px;width:82px;text-align:justify;font-size:4.8px">Identifying new opportunities, and emerging needs, for the delivery of innovative knowledge-solutions in the Fintech space.</div>
  <div class="foot"></div>
</section>

<!-- 22 publications -->
<section class="slide c1 r8">
  <div class="photo" role="img" aria-label="Stack of printed journals" style="left:0;top:0;width:109px;height:138px;background:linear-gradient(135deg,#5c6874,#2f3842)"></div>
  <div class="abs ctr" style="left:0;top:50px;width:109px;color:#fff;font-weight:700;font-size:11px;line-height:1.3">PUBLICATIONS<br>SERVICES</div>
  <svg class="abs" style="left:110px;top:0" width="136" height="138" viewBox="0 0 136 138">
    <polygon points="68,14 94,14 81,60" fill="var(--green)" transform="translate(-13,0)"/>
    <polygon points="38,20 62,62 14,62" fill="var(--olive)"/>
    <polygon points="98,20 122,62 74,62" fill="var(--green-dark)"/>
    <polygon points="14,66 62,66 38,108" fill="var(--green-dark)"/>
    <polygon points="74,66 122,66 98,108" fill="var(--olive)"/>
    <polygon points="68,70 90,112 46,112" fill="var(--green)"/>
    <g font-size="4.5" fill="#fff" text-anchor="middle" font-weight="500"><text x="68" y="24">Books</text><text x="38" y="56">eBooks</text><text x="98" y="56">Journals</text><text x="38" y="76">Pamphlets</text><text x="98" y="78">Reports</text><text x="68" y="108">Online material</text></g>
    <g fill="none" stroke="#fff" stroke-width=".8"><rect x="34" y="36" width="8" height="10"/><rect x="94" y="36" width="8" height="10"/><rect x="34" y="84" width="8" height="8"/><rect x="94" y="84" width="8" height="8"/><rect x="64" y="30" width="8" height="7"/><rect x="64" y="88" width="8" height="8"/></g>
  </svg>
  <div class="foot"></div>
</section>

<!-- 23 books -->
<section class="slide c2 r8">
  <div class="title" style="top:8px">BOOKS</div>
  <svg class="abs" style="left:0;top:0" width="246" height="138" viewBox="0 0 246 138" role="img" aria-label="Grid of book covers">
    <g>
      <rect x="32" y="25" width="25" height="29" fill="#2d5d8a"/><rect x="64" y="25" width="25" height="29" fill="#b9845a"/><rect x="96" y="25" width="25" height="29" fill="#e8e3dc"/><rect x="128" y="25" width="25" height="29" fill="#d9d4cd"/><rect x="160" y="25" width="25" height="29" fill="#e07b4a"/><rect x="192" y="25" width="25" height="29" fill="#6e9fc9"/>
      <rect x="32" y="57" width="25" height="29" fill="#b5894a"/><rect x="64" y="57" width="25" height="29" fill="#c98a2a"/><rect x="96" y="57" width="25" height="29" fill="#ece8de"/><rect x="128" y="57" width="25" height="29" fill="#d8a52b"/><rect x="160" y="57" width="25" height="29" fill="#6d8ea3"/><rect x="192" y="57" width="25" height="29" fill="#8a6a3a"/>
      <rect x="32" y="89" width="25" height="29" fill="#d99a3c"/><rect x="64" y="89" width="25" height="29" fill="#4a3a2d"/><rect x="96" y="89" width="25" height="29" fill="#5aa04a"/><rect x="128" y="89" width="25" height="29" fill="#2f8a4c"/><rect x="160" y="89" width="25" height="29" fill="#d7dbd9"/><rect x="192" y="89" width="25" height="29" fill="#5a7ca0"/>
    </g>
  </svg>
  <div class="foot"></div>
</section>

<!-- 24 contact -->
<section class="slide c3 r8">
  <div class="abs ctr" style="left:0;right:0;top:8px;font-weight:500;font-size:13.5px;color:var(--green-dark)">Get in touch via</div>
  <div class="photo" role="img" aria-label="Dark textured background" style="left:0;top:30px;width:246px;height:100px;background:linear-gradient(135deg,#2c2f33,#45494e 50%,#2a2d31)"></div>
  <div class="abs" style="left:15px;top:68px;color:#fff;font-weight:700;font-size:14px">THANK YOU!</div>
  <div class="abs" style="left:6px;top:110px;color:#fff;font-size:3px">VOLMA &nbsp; VOLMAKSA</div>
  <svg class="abs" style="left:6px;top:114px" width="60" height="10" viewBox="0 0 60 10"><g fill="#fff"><circle cx="5" cy="5" r="4"/><circle cx="21" cy="5" r="4"/><circle cx="37" cy="5" r="4"/><circle cx="53" cy="5" r="4"/></g></svg>
  <svg class="abs" style="left:130px;top:38px" width="110" height="86" viewBox="0 0 110 86">
    <g fill="#fff" stroke="var(--green)" stroke-width="1.5"><circle cx="9" cy="8" r="6"/><circle cx="9" cy="27" r="6"/><circle cx="9" cy="46" r="6"/><circle cx="9" cy="65" r="6"/></g>
    <g stroke="var(--green-dark)" fill="none" stroke-width=".9"><path d="M6.5,5.5c0,3 2,5 5,5"/><rect x="6" y="25" width="6" height="4"/><circle cx="9" cy="46" r="3"/><path d="M6,46h6M9,43v6"/><rect x="6.5" y="62" width="5" height="6"/></g>
    <g stroke="#8a8a8a" stroke-width=".4"><path d="M20,17h88M20,36h88M20,55h88M20,74h88"/></g>
    <g font-size="4" fill="#fff"><text x="20" y="10">+966 10 555 0140</text><text x="20" y="29">info@volma.org</text><text x="20" y="48">www.volma.org</text><text x="20" y="67">+966 10 555 0892</text></g>
  </svg>
  <div class="foot"></div>
</section>

</div>
</body>
</html>
```